Business Card Design - Kestrel Tidewave

We (Kestrel Tidewave) need a business card design for our boutique mobile marketing agency based in Sydney, Australia.
We work with brands and advertisers to deliver and implement end to end mobile (smartphone and tablet) marketing solutions.

We already have a logo and website design, these files will be provided. Our colours centre around a blue/orange mix (the logo containing the orange (colour code: RGB 255,165,0).

Our name and logo communicate strength and confidence. We see ourselves as being trustworthy advisors who are also fun and passionate.

Target Market(s)

Senior Marketing Managers

Industry/Entity Type

Marketing

Requirements
Must have
• Employee Name: Dara Linwood
Mobile Number: 0400 555 182
Email Address xxxx@kestreltidewave.example
Website: www.kestreltidewave.example
Twitter ID: KestrelTidewave

```html
<!DOCTYPE html>
<html lang="en">
<head>
<meta charset="utf-8">
<title>Kestrel Tidewave – Business Card</title>
<link href="https://fonts.googleapis.com/css2?family=Open+Sans:wght@400;600;700&display=swap" rel="stylesheet">
<style>
  :root {
    --page-bg: #e9ecef;
    --sky-top: #8ec5ee;
    --sky-mid: #cfe6f8;
    --card-white: #ffffff;
    --ink: #3a3a3c;
    --ink-soft: #4a4a4d;
    --accent-orange: #f04a1a;
    --mascot-blue: #2b88cc;
  }
  * { box-sizing: border-box; margin: 0; padding: 0; }
  html, body {
    width: 1200px; height: 821px; overflow: hidden;
    background: var(--page-bg);
    font-family: "Open Sans", Arial, sans-serif;
    color: var(--ink);
  }
  .stage {
    position: relative; width: 1200px; height: 821px;
    display: flex; align-items: center; justify-content: center; gap: 40px;
  }
  .card {
    position: relative; width: 540px; height: 310px;
    border-radius: 16px; overflow: hidden;
    background: linear-gradient(to bottom, var(--sky-top) 0%, var(--sky-mid) 45%, var(--card-white) 85%);
    box-shadow: 0 6px 18px rgba(0,0,0,0.18);
  }
  .brand {
    display: flex; align-items: center; gap: 10px;
    color: var(--ink); font-weight: 700; letter-spacing: 0.5px;
    white-space: nowrap;
  }
  .brand-dot {
    flex: none; border-radius: 50%; background: var(--accent-orange);
  }
  /* front */
  .card-front .brand { position: absolute; left: 30px; top: 42px; font-size: 28px; }
  .card-front .brand-dot { width: 30px; height: 30px; }
  .person-name {
    position: absolute; left: 34px; top: 140px;
    font-size: 24px; font-weight: 600; color: var(--ink-soft);
  }
  .contact-list {
    position: absolute; left: 34px; top: 184px; list-style: none;
    font-size: 16px; color: var(--ink-soft);
  }
  .contact-list li { display: flex; align-items: center; gap: 10px; height: 24px; white-space: nowrap; }
  .contact-icon { width: 16px; height: 16px; flex: none; }
  .mascot-area {
    position: absolute; right: 30px; top: 80px; width: 170px; height: 190px;
    border-radius: 85px 85px 24px 24px;
    background: radial-gradient(circle at 50% 40%, var(--mascot-blue) 0%, #5aa6de 70%, rgba(90,166,222,0) 100%);
  }
  /* back */
  .card-back .brand {
    position: absolute; left: 0; right: 0; top: 118px;
    justify-content: center; font-size: 34px;
  }
  .card-back .brand-dot { width: 36px; height: 36px; }
  .website-line {
    position: absolute; left: 0; right: 0; bottom: 38px;
    text-align: center; font-size: 17px; font-weight: 600; color: var(--ink);
  }
</style>
</head>
<body>
<main class="stage">
  <section class="card card-front">
    <div class="brand"><span class="brand-dot"></span><span>Kestrel Tidewave</span></div>
    <div class="person-name">Dara Linwood</div>
    <ul class="contact-list">
      <li>
        <svg class="contact-icon" viewBox="0 0 16 16"><rect x="4" y="1" width="8" height="14" rx="1.5" fill="var(--accent-orange)"/><rect x="5.5" y="3" width="5" height="6" fill="#fff"/></svg>
        0400 555 182
      </li>
      <li>
        <svg class="contact-icon" viewBox="0 0 16 16"><rect x="1" y="3" width="14" height="10" rx="1" fill="var(--accent-orange)"/><path d="M1.5 3.5 8 9l6.5-5.5" stroke="#fff" stroke-width="1.4" fill="none"/></svg>
        dara@kestreltidewave.example
      </li>
      <li>
        <svg class="contact-icon" viewBox="0 0 16 16"><circle cx="8" cy="8" r="7" fill="var(--accent-orange)"/><g stroke="#fff" stroke-width="1" fill="none"><ellipse cx="8" cy="8" rx="3" ry="6.5"/><path d="M1.5 8h13M2.5 5h11M2.5 11h11"/></g></svg>
        www.kestreltidewave.example
      </li>
      <li>
        <svg class="contact-icon" viewBox="0 0 16 16"><rect x="1" y="1" width="14" height="14" rx="3" fill="var(--accent-orange)"/></svg>
        KestrelTidewave
      </li>
    </ul>
    <div class="mascot-area" role="img" aria-label="Blue cartoon mascot with antenna waving and holding a mobile phone"></div>
  </section>

  <section class="card card-back">
    <div class="brand"><span class="brand-dot"></span><span>Kestrel Tidewave</span></div>
    <div class="website-line">www.kestreltidewave.example</div>
  </section>
</main>
</body>
</html>
```